Bravel Acres Business Cards

design business cards for our new business should match my Corvane Quotations business cards

Contact Information for Business Card

2817 W 68th N St
Tulsa, OK 74592

Requirements
Must have
• should match logo colors

```html
<!DOCTYPE html>
<html lang="en">
<head>
<meta charset="utf-8">
<title>Bravel Acres Business Cards</title>
<link rel="stylesheet" href="https://fonts.googleapis.com/css2?family=Open+Sans:wght@400;600&display=swap">
<style>
  :root {
    --backdrop: #3a3d41;
    --card: #072b33;
    --leaf-green: #7dc242;
    --aqua: #0ab0b8;
    --paper: #f2f2f2;
  }
  * { margin: 0; padding: 0; box-sizing: border-box; }
  html, body { width: 1200px; height: 900px; overflow: hidden; }
  body {
    background: var(--backdrop);
    font-family: "Open Sans", Arial, sans-serif;
    position: relative;
  }
  .card {
    position: absolute;
    left: 320px;
    width: 560px;
    height: 320px;
    border-radius: 18px;
    background: var(--card);
    overflow: hidden;
  }
  .card--front { top: 110px; }
  .card--back { top: 470px; }

  .brand {
    position: absolute;
    display: flex;
    align-items: center;
    gap: 14px;
  }
  .brand__dot {
    width: 22px; height: 22px;
    border-radius: 50%;
    background: var(--leaf-green);
  }
  .brand__name {
    font-weight: 600;
    font-size: 38px;
    letter-spacing: 0.04em;
    color: var(--leaf-green);
    white-space: nowrap;
  }
  .card--front .brand {
    left: 50%; top: 50%;
    transform: translate(-50%, -50%);
  }
  .card--back .brand {
    left: 34px; top: 108px;
  }
  .brand--compact .brand__name { font-size: 32px; }

  .divider {
    position: absolute;
    left: 318px; top: 46px;
    width: 1px; height: 150px;
    background: linear-gradient(var(--aqua), var(--leaf-green));
  }
  .address {
    position: absolute;
    left: 342px; top: 58px;
    display: flex;
    align-items: flex-start;
    gap: 8px;
    font-size: 14px;
    line-height: 1.3;
  }
  .address__icon { width: 14px; height: 14px; margin-top: 8px; }
  .address__lines span { display: block; }
  .address__street { color: var(--aqua); }
  .address__city { color: var(--leaf-green); }

  .band-light {
    position: absolute;
    left: 0; bottom: 0;
    width: 318px; height: 22px;
    background: var(--paper);
  }
  .band-accent {
    position: absolute;
    right: 0; bottom: 0;
    width: 228px; height: 64px;
    background: linear-gradient(60deg, var(--leaf-green) 35%, var(--aqua) 75%);
  }
</style>
</head>
<body>
  <section class="card card--front" aria-label="Card front">
    <div class="brand">
      <span class="brand__dot"></span>
      <span class="brand__name">Bravel Acres</span>
    </div>
  </section>

  <section class="card card--back" aria-label="Card back">
    <div class="brand brand--compact">
      <span class="brand__dot"></span>
      <span class="brand__name">Bravel Acres</span>
    </div>
    <div class="divider"></div>
    <div class="address">
      <svg class="address__icon" viewBox="0 0 16 16" aria-hidden="true">
        <path d="M8 1 L15 7.5 L13 7.5 L13 15 L9.5 15 L9.5 10.5 L6.5 10.5 L6.5 15 L3 15 L3 7.5 L1 7.5 Z" fill="#ffffff"/>
      </svg>
      <div class="address__lines">
        <span class="address__street">2817 W 68th N St</span>
        <span class="address__city">Tulsa, OK 74592</span>
      </div>
    </div>
    <div class="band-light"></div>
    <div class="band-accent"></div>
  </section>
</body>
</html>
```